International Film making Business needs the 5 Logos provided made into a POSTER Format

Design Task:
CREATE A POSTER DESIGN USING THE 5 LOGOS PROVIDED. The GLAD SKY VISTA LOGO should stand out from the others by being in the middle with the other 4 logos connected to it somehow.

The 5 Businesses already has their 5 Logos, all similar in design to each other.

GLAD SKY VISTA is the Main Logo that encompasses the other 4 Logos. So it must stand out more and it is like the Overall Business entity that incorporates the other 4 Logos.

What is required is that by using the 5 Logo designs provided, create a cool graphic artwork that somehow incorporates ALL of the 5 Logos - But having the GLAD SKY VISTA Logo at the forefront/most important/standing out the most.
- GLAD SKY VISTA will probably be bigger than the others
- and could be changed into 3D.

I have attached all 5 logos and a hand drawn example of how the GLAD SKY VISTAS could stand out from the rest.

THE DESIGNS OF THE LOGOS SHOULD NOT BE CHANGED (except the GLADSKYVISTA which can be 3D)

Please do not be restricted with the sample idea. Creativity is encouraged

DIMENSION: 3000 mm x 6000 mm
high resolution graphic

Logo Text

glad sky , glad sky reels, glad sky tales, glad sky groovy, GLAD SKY VISTAS

Requirements
Must have
• USE THE 5 LOGOS PROVIDED ONLY - Only GLAD SKY VISTA can be changed into 3D only
Nice to have
• Eye catching design, showing the Glad Sky Vista as the most powerful Logo that has the other 4 as subordinate companies
Should not have
• ANY CHANGE IN THE 5 LOGO DESIGNS (EXcept 3D for Glad Sky Vistas)

```html
<!DOCTYPE html>
<html lang="en">
<head>
<meta charset="utf-8">
<title>Glad Sky Vistas Poster</title>
<link rel="stylesheet" href="https://fonts.googleapis.com/css2?family=Marcellus&family=Nunito+Sans:wght@400&display=swap">
<style>
  :root {
    --bg-plum: #3b0f2e;
    --bg-deep: #22152a;
    --bg-teal: #1b2b2b;
    --pink: #ee3a94;
    --orange: #f7b468;
    --violet: #8a5cc0;
    --cyan: #5fd0d8;
    --sun: #ffc65e;
    --board: #070506;
    --gold: #d9ad4a;
    --silver: #b9b9bb;
    --blue: #2a9ee0;
    --spectrum: #e85a7a;
    --green: #3fa84a;
    --steel: #9c9c9e;
  }
  * { margin: 0; padding: 0; box-sizing: border-box; }
  html, body { width: 1200px; height: 600px; overflow: hidden; background: var(--bg-deep); }
  .poster {
    position: relative;
    width: 1200px;
    height: 600px;
    overflow: hidden;
    background: linear-gradient(100deg, var(--bg-plum) 0%, var(--bg-deep) 45%, var(--bg-teal) 100%);
    font-family: "Marcellus", serif;
  }
  .backdrop { position: absolute; inset: 0; }
  .brand {
    position: absolute;
    display: flex;
    align-items: center;
    gap: 14px;
    text-transform: uppercase;
    line-height: 1.02;
    letter-spacing: 2px;
  }
  .brand-mark {
    flex: none;
    border-radius: 50%;
    border: 3px solid currentColor;
  }
  .brand-name { font-weight: 400; }
  .brand--root { left: 80px; top: 185px; color: var(--blue); font-size: 38px; }
  .brand--root .brand-mark { width: 90px; height: 90px; }
  .brand--tales { left: 520px; top: 40px; color: var(--spectrum); font-size: 36px; }
  .brand--tales .brand-mark { width: 86px; height: 86px; }
  .brand--vistas { left: 410px; top: 262px; color: var(--gold); font-size: 46px; }
  .brand--vistas .brand-mark { width: 130px; height: 130px; }
  .brand--reels { left: 395px; top: 470px; color: var(--steel); font-size: 34px; }
  .brand--reels .brand-mark { width: 90px; height: 90px; }
  .brand--groovy {
    left: 900px; top: 255px; width: 230px;
    flex-direction: column; gap: 14px; text-align: center;
    color: var(--green); font-size: 36px;
  }
  .brand--groovy .brand-mark { width: 90px; height: 90px; }
  .vistas-url {
    display: block;
    margin-top: 8px;
    font-family: "Nunito Sans", sans-serif;
    font-size: 14px;
    letter-spacing: 2px;
    text-transform: none;
    color: var(--silver);
  }
</style>
</head>
<body>
<main class="poster">
  <svg class="backdrop" width="1200" height="600" viewBox="0 0 1200 600" aria-hidden="true">
    <defs>
      <linearGradient id="corner-violet" x1="0" y1="0" x2="0" y2="1">
        <stop offset="0" stop-color="#7d5bb8"/>
        <stop offset="1" stop-color="#3d54a8"/>
      </linearGradient>
    </defs>
    <!-- corner wedges -->
    <polygon points="0,400 200,600 0,600" fill="url(#corner-violet)"/>
    <polygon points="1030,0 1200,0 1200,180" fill="var(--sun)"/>
    <polygon points="1010,600 1200,440 1200,600" fill="var(--cyan)" opacity="0.9"/>
    <!-- film bands -->
    <g fill="none" stroke-width="30" stroke-linecap="square" opacity="0.9">
      <line x1="290" y1="-10" x2="650" y2="290" stroke="var(--pink)"/>
      <line x1="1080" y1="-10" x2="760" y2="250" stroke="var(--orange)"/>
      <line x1="-10" y1="360" x2="170" y2="510" stroke="var(--violet)"/>
      <line x1="170" y1="600" x2="420" y2="340" stroke="var(--violet)" opacity="0.8"/>
      <line x1="1210" y1="450" x2="760" y2="610" stroke="var(--cyan)"/>
    </g>
    <!-- clapperboard -->
    <g role="img" aria-label="Film clapperboard">
      <polygon points="392,142 845,130 850,205 396,222" fill="var(--board)" opacity="0.75"/>
      <rect x="392" y="222" width="461" height="224" fill="var(--board)" opacity="0.92"/>
    </g>
  </svg>

  <div class="brand brand--tales">
    <span class="brand-mark"></span>
    <span class="brand-name">Glad Sky<br>Tales</span>
  </div>

  <div class="brand brand--root">
    <span class="brand-mark"></span>
    <span class="brand-name">Glad<br>Sky</span>
  </div>

  <div class="brand brand--vistas">
    <span class="brand-mark"></span>
    <span class="brand-name">Glad Sky<br>Vistas
      <span class="vistas-url">gladskyvistas.example</span>
    </span>
  </div>

  <div class="brand brand--groovy">
    <span class="brand-mark"></span>
    <span class="brand-name">Glad Sky<br>Groovy</span>
  </div>

  <div class="brand brand--reels">
    <span class="brand-mark"></span>
    <span class="brand-name">Glad Sky<br>Reels</span>
  </div>
</main>
</body>
</html>
```